Banner ad design for Vantor Reach Ads

We are looking for a designer to develop a concept for banner ads for a Vantor Reach campaign we are building.

We have 3 business lines, shredding services, records management services and scanning services.

We are looking for 4 sets of ads to be created, one for each business line + one set that showcases all of our lines together.

For the design concepts, we would like to see a few sizes (banner, square, leaderboard, skyscraper, etc) for each.

The person chosen will then need to create the ads into all Vantor supported sizes -- 20 sizes total for each set of ads as per the Vantor size guidelines found on this page - https://help.vantor.example/vantor-ads/answer/4859210?hl=en&ref_topic=6082714#

A few items to note:
- Design should complement our existing brand/website look and feel (www.gold-kettle.ca)
- Each final ad must be 150Kb or less in size
- Final designs should be editable, meaning if we would like to change some copy in the design, we can do so using a well-known software (Canva, Photoshop/InDesign, etc)
- Some images are attached for use, but if you feel a different stock image is more suitable to to your design, please go ahead and use it.

Provided below is some messaging that can be used for each set of ads. Do not feel you need to use all of the messaging, it is provided for guidance.

SHREDDING SERVICES:

Possible Short Headline:
-- One-Time Shredding Services
-- Secure Shredding Services
-- Affordable On-Site Shredding

Possible Long Headline
-- Your Paper Can be Destroyed as Soon as the Next Business Day

Possible Descriptions:
-- QVRB AAA Certified On site shredding company. Service as soon as Next Day.
-- Secure and Affordable Toronto & GTA On-Site Shredding.
-- Certified, Affordable Office Shredding Since 2003.
-- Quick, no contact and affordable paper shredding services in Toronto & Southern Ontario.
-- Certified, Affordable Office Shredding Since 2003. Fast, no contact shredding service.

Call to Action
-- Get a Quote

RECORDS MANAGEMENT
Short Headline:
-- Off-site Records Storage
-- Records Management & Storage
-- Secure Records Storage
-- Records Management Services
-- Long Term Records Management
-- Document Storage Solutions

Possible Description
-- Local, Affordable Storage Solutions. Protect and Store your Documents in our Secure Facility
-- Local, Affordable Records Management Solutions. Store your Records in our Secure Facility
-- Certified, Affordable Document Storage Since 2004. Contact Us for a Free Quote!
-- Vaultmark+ Certified, Affordable Document Storage Since 2004. Contact Us for a Free Quote!

Call to Action
-- Get a Quote

SCANNING SERVICES

Short Headline:
-- Professional Scanning Company
-- Toronto & GTA Scanning Service
-- Document Scanning Services
-- Digital Conversion Services
-- Fast & Easy Retrieval

Description
-- Scan and documents and files with Professional scanning services from Gold-Kettle
-- Convert Your Paper Files to Electronic Files. Fast & Easy Retrieval.
-- Easily access your documents electronically with Document Scanning Services

Call to Action
-- Get a Quote

ALL SERVICES AD SET
Short Headline
-- Shred, Scan & Store Documents
-- Secure Shredding, Records Management and Scanning Services
-- #1 Document Management Company
-- Gold Kettle Shredding, Storage & Scanning

Description
-- Secure and Affordable Toronto & GTA On-Site Shredding, Document Storage & Scanning Company

Call to Action
-- Get a Quote

Font styles to use
Sans Serif

```html
<!DOCTYPE html>
<html lang="en">
<head>
<meta charset="utf-8">
<title>Gold-Kettle Ads</title>
<link href="https://fonts.googleapis.com/css2?family=Montserrat:wght@500;600;700;800&display=swap" rel="stylesheet">
<style>
  :root {
    --board-blue: #0a98cf;
    --panel-blue: #0b93cb;
    --cta-green: #12b847;
    --white: #ffffff;
    --ink: #1c2630;
    --card-edge: #101418;
  }
  * { box-sizing: border-box; margin: 0; padding: 0; }
  html, body { width: 1200px; height: 1080px; overflow: hidden; }
  body {
    background: var(--board-blue);
    font-family: "Montserrat", Arial, sans-serif;
    color: var(--white);
    position: relative;
  }
  .board-title {
    position: absolute; top: 36px; left: 0; width: 1200px;
    text-align: center; font-weight: 800; font-size: 62px; letter-spacing: 0.5px; line-height: 1;
  }
  .board-footer {
    position: absolute; top: 994px; left: 0; width: 1200px;
    text-align: center; font-weight: 800; font-size: 27px; line-height: 1;
  }
  .ad {
    position: absolute; width: 449px; height: 374px;
    background: var(--panel-blue);
    border: 1.5px solid var(--card-edge);
    box-shadow: 0 8px 14px rgba(0,0,0,0.35);
    overflow: hidden;
  }
  .ad--storage { left: 130px; top: 143px; }
  .ad--shredding { left: 620px; top: 143px; }
  .ad--scanning { left: 130px; top: 565px; }
  .ad--all { left: 620px; top: 565px; }
  .ad__header { position: absolute; left: 0; top: 0; width: 100%; height: 81px; background: var(--white); }
  .ad--shredding .ad__header, .ad--scanning .ad__header, .ad--all .ad__header { height: 74px; }
  .ad__photo { position: absolute; left: 0; top: 0; width: 449px; height: 374px; }
  .brand { position: absolute; left: 20px; top: 26px; color: var(--ink); }
  .ad--shredding .brand { top: 22px; }
  .ad--scanning .brand, .ad--all .brand { top: 24px; left: 24px; }
  .ad--all .brand { left: 14px; }
  .brand__name { display: flex; align-items: center; gap: 5px; font-weight: 800; font-size: 22px; line-height: 1; letter-spacing: -0.3px; }
  .brand__dot { width: 9px; height: 9px; border-radius: 50%; background: var(--panel-blue); }
  .brand__tagline { font-weight: 500; font-size: 12.5px; margin-top: 4px; letter-spacing: 0.3px; }
  .ad__headline { position: absolute; font-weight: 800; text-transform: uppercase; }
  .ad--storage .ad__headline { left: 18px; top: 98px; font-size: 36px; line-height: 36px; }
  .ad--shredding .ad__headline { left: 13px; top: 86px; font-size: 30px; line-height: 30px; }
  .ad--scanning .ad__headline { left: 16px; top: 108px; font-size: 30px; line-height: 30px; }
  .ad--scanning .ad__kicker { display: block; font-size: 20px; line-height: 24px; }
  .ad--all .ad__headline { left: 14px; top: 96px; font-size: 30px; line-height: 30px; }
  .ad__rule { position: absolute; height: 2px; width: 137px; background: var(--white); }
  .ad--storage .ad__rule { left: 20px; top: 217px; }
  .ad--shredding .ad__rule { left: 14px; top: 191px; }
  .ad--scanning .ad__rule { left: 18px; top: 205px; }
  .ad--all .ad__rule { left: 15px; top: 214px; }
  .ad__body { position: absolute; font-weight: 500; }
  .ad--storage .ad__body { left: 20px; top: 229px; width: 215px; font-size: 15.5px; line-height: 19.5px; }
  .ad--shredding .ad__body { left: 12px; top: 204px; width: 190px; font-size: 16px; line-height: 20px; }
  .ad--scanning .ad__body { left: 16px; top: 222px; width: 180px; font-size: 13.5px; line-height: 16px; }
  .ad--all .ad__body { left: 13px; top: 232px; width: 215px; font-size: 13.3px; line-height: 16px; }
  .ad__cta {
    position: absolute; top: 317px; width: 182px; height: 38px;
    background: var(--cta-green); color: var(--white);
    font-weight: 800; font-size: 18px; line-height: 38px; text-align: center; letter-spacing: 0.3px;
  }
  .ad--storage .ad__cta { left: 20px; top: 318px; }
  .ad--shredding .ad__cta { left: 12px; }
  .ad--scanning .ad__cta { left: 16px; }
  .ad--all .ad__cta { left: 13px; }
</style>
</head>
<body>
  <h1 class="board-title">GOLD-KETTLE ADS</h1>

  <section class="ad ad--storage">
    <div class="ad__header"></div>
    <svg class="ad__photo" viewBox="0 0 449 374" role="img" aria-label="Photo of a tall records warehouse with blue racking full of archive boxes">
      <defs>
        <linearGradient id="warehouse-tone" x1="0" y1="0" x2="1" y2="1">
          <stop offset="0" stop-color="#6b5f57"/>
          <stop offset="0.45" stop-color="#b9a58c"/>
          <stop offset="0.75" stop-color="#2f4f9a"/>
          <stop offset="1" stop-color="#c9c3b4"/>
        </linearGradient>
      </defs>
      <path d="M222 58 Q449 -6 449 -6 L449 374 L286 374 L213 84 Q210 64 222 58 Z" fill="url(#warehouse-tone)" stroke="#ffffff" stroke-width="3"/>
    </svg>
    <div class="brand">
      <div class="brand__name">gold-kettle<span class="brand__dot"></span></div>
      <div class="brand__tagline">Information Security</div>
    </div>
    <h2 class="ad__headline">Off-Site<br>Records<br>Storage</h2>
    <div class="ad__rule"></div>
    <p class="ad__body">Local, Affordable Storage Solutions. Protect and Store your Documents in our Secure Facility</p>
    <div class="ad__cta">GET A QUOTE</div>
  </section>

  <section class="ad ad--shredding">
    <div class="ad__header"></div>
    <svg class="ad__photo" viewBox="0 0 449 374" role="img" aria-label="Photo of a baled stack of shredded white paper">
      <defs>
        <linearGradient id="shred-tone" x1="0" y1="0" x2="0" y2="1">
          <stop offset="0" stop-color="#b8b8b4"/>
          <stop offset="0.35" stop-color="#e9e9e7"/>
          <stop offset="0.75" stop-color="#d2d3d1"/>
          <stop offset="1" stop-color="#8a8b88"/>
        </linearGradient>
      </defs>
      <path d="M253 0 L449 0 L449 374 L253 374 L190 187 Z" fill="url(#shred-tone)" stroke="#ffffff" stroke-width="3"/>
    </svg>
    <div class="brand">
      <div class="brand__name">gold-kettle<span class="brand__dot"></span></div>
      <div class="brand__tagline">Information Security</div>
    </div>
    <h2 class="ad__headline">One-Time<br>Shredding<br>Services</h2>
    <div class="ad__rule"></div>
    <p class="ad__body">Quick, no contact and affordable paper shredding services in Toronto &amp; Southern Ontario</p>
    <div class="ad__cta">GET A QUOTE</div>
  </section>

  <section class="ad ad--scanning">
    <div class="ad__header"></div>
    <svg class="ad__photo" viewBox="0 0 449 374" role="img" aria-label="Blue-toned photo of a hand pressing the keypad of an office scanner">
      <defs>
        <linearGradient id="scanner-tone" x1="0" y1="0" x2="1" y2="1">
          <stop offset="0" stop-color="#eef3f8"/>
          <stop offset="0.4" stop-color="#b4c6da"/>
          <stop offset="0.7" stop-color="#7f97b3"/>
          <stop offset="1" stop-color="#a9bbcf"/>
        </linearGradient>
      </defs>
      <path d="M290 0 L449 0 L449 374 L330 374 C230 320 185 240 196 170 C205 100 240 40 290 0 Z" fill="url(#scanner-tone)" stroke="#ffffff" stroke-width="3"/>
    </svg>
    <div class="brand">
      <div class="brand__name">gold-kettle<span class="brand__dot"></span></div>
      <div class="brand__tagline">Information Security</div>
    </div>
    <h2 class="ad__headline"><span class="ad__kicker">Professional</span>Scanning<br>Company</h2>
    <div class="ad__rule"></div>
    <p class="ad__body">can and documents and files with Professional scanning services from Gold-Kettle</p>
    <div class="ad__cta">GET A QUOTE</div>
  </section>

  <section class="ad ad--all">
    <div class="ad__header"></div>
    <svg class="ad__photo" viewBox="0 0 449 374" role="img" aria-label="Photo of tall stacks of paper files with coloured tabs">
      <defs>
        <linearGradient id="files-tone" x1="0" y1="0" x2="1" y2="1">
          <stop offset="0" stop-color="#8c8684"/>
          <stop offset="0.35" stop-color="#d9d3cf"/>
          <stop offset="0.55" stop-color="#e7b4c6"/>
          <stop offset="0.75" stop-color="#ece2a8"/>
          <stop offset="1" stop-color="#7d7a78"/>
        </linearGradient>
      </defs>
      <rect x="240" y="0" width="209" height="374" fill="url(#files-tone)"/>
      <rect x="238" y="0" width="2" height="374" fill="#ffffff"/>
    </svg>
    <div class="brand">
      <div class="brand__name">gold-kettle<span class="brand__dot"></span></div>
      <div class="brand__tagline">Information Security</div>
    </div>
    <h2 class="ad__headline">Shred, Scan<br>&amp; Store<br>Documents</h2>
    <div class="ad__rule"></div>
    <p class="ad__body">Secure and Affordable Toronto &amp; GTA On-Site Shredding, Document Storage &amp; Scanning Company</p>
    <div class="ad__cta">GET A QUOTE</div>
  </section>

  <p class="board-footer">WILL BE ADJUSTED TO THE 20 SIZES YOU ARE LOOKING FOR</p>
</body>
</html>
```